Speisekarten
Zielgruppe
Die Sola Brisa Kassel ist vorrangig in der hochwertigen Gastronomie und Hotellerie tätig. Unser Leitspruch: IMMER EINEN TICK MEHR ALS ERWARTET. MEHR QUALITÄT, MEHR VIELFALT, MEHR LEISTUNG, MEHR LEIDENSCHAFT IN JEDEM DETAIL.
Was dazu gehört: Eine vielseitige Genießerwelt, die ihresgleichen sucht: Zehn Event-Locations, drei Hotels, zwanzig Tagungsräume, sieben Restaurants, eine Eisbar, zwei Feinkostgeschäfte und einen eigenen Strandabschnitt an der Lahn dürfen wir zu uns zählen.
Ob tagen, erholen, feiern oder genießen, bei uns gibt es das Rundum-Paket.
Aufgabenstellung
Sehr hochwertiges Design einer Speisekarte für ein asiatisches Restaurant der Extraklasse.

```html
<!DOCTYPE html>
<html lang="de">
<head>
<meta charset="utf-8">
<title>Hoshiba – Speisekarte</title>
<link href="https://fonts.googleapis.com/css2?family=Josefin+Sans:wght@400;700&display=swap" rel="stylesheet">
<style>
  :root {
    --backdrop: #141414;
    --paper: #ffffff;
    --ink: #111111;
    --rule: #6e6e6e;
    --accent: #d2321e;
    --placeholder: #e4e4e4;
  }
  * { margin: 0; padding: 0; box-sizing: border-box; }
  html, body { width: 686px; height: 1200px; overflow: hidden; background: var(--backdrop); }
  .canvas { position: relative; width: 686px; height: 1200px; font-family: "Josefin Sans", sans-serif; color: var(--ink); }
  .page { position: absolute; width: 325px; background: var(--paper); }
  .page--tl { left: 19px; top: 19px; height: 580px; }
  .page--tr { left: 344px; top: 19px; height: 580px; }
  .page--bl { left: 19px; top: 606px; height: 578px; }
  .page--br { left: 344px; top: 606px; height: 578px; }

  .rule { position: absolute; height: 0; border-top: 0.6px solid var(--rule); top: 104px; }
  .script-title { position: absolute; top: 94px; height: 20px; background: var(--placeholder); border-radius: 2px; }

  .brand { position: absolute; top: 96px; left: 132px; width: 66px; display: flex; align-items: center; justify-content: center; gap: 4px; }
  .brand__name { font-size: 9px; font-weight: 700; letter-spacing: 1.2px; color: var(--ink); }
  .brand__square { width: 6px; height: 6px; background: var(--accent); }

  .section-intro { position: absolute; top: 121px; left: 0; width: 100%; text-align: center; font-size: 6px; letter-spacing: 0.3px; font-variant: small-caps; text-transform: lowercase; }
  .section-label { position: absolute; left: 0; width: 100%; text-align: center; font-size: 5.6px; font-weight: 700; letter-spacing: 0.4px; }

  .dish { position: absolute; left: 46px; right: 48px; }
  .dish__head { display: flex; justify-content: space-between; font-size: 5.6px; line-height: 8px; letter-spacing: 0.4px; }
  .dish__name { font-weight: 700; }
  .dish__note { font-weight: 400; }
  .dish__price { font-weight: 400; }
  .dish__desc { margin-top: 5px; font-size: 6px; line-height: 13px; letter-spacing: 0.3px; font-variant: small-caps; text-transform: lowercase; }
  .dish__desc .caps { text-transform: none; }

  .illustration { position: absolute; left: 120px; top: 439px; width: 72px; height: 78px; background: var(--placeholder); border-radius: 3px; }
</style>
</head>
<body>
<div class="canvas">

  <!-- Vorspeisen: Suppen -->
  <section class="page page--tl">
    <div class="rule" style="left:46px; width:85px;"></div>
    <div class="script-title" role="img" aria-label="Handgeschriebener Schriftzug „starter“" style="left:138px; width:50px;"></div>
    <div class="rule" style="left:193px; width:85px;"></div>

    <div class="section-label" style="top:200px;">SOUP</div>

    <article class="dish" style="top:255px;">
      <div class="dish__head"><span class="dish__name">MISOSUPPE</span><span class="dish__price">6,0</span></div>
      <p class="dish__desc">Tofu | Alge | Lauchzwiebel | Sesam</p>
    </article>
    <article class="dish" style="top:334px;">
      <div class="dish__head"><span class="dish__name">KOKOSSUPPE</span><span class="dish__price">8,5</span></div>
      <p class="dish__desc">Garnele | Champignon | Bambusstreifen | Koriander</p>
    </article>
    <article class="dish" style="top:413px;">
      <div class="dish__head"><span class="dish__name">JAPANISCHE HÜHNERSUPPE</span><span class="dish__price">7,5</span></div>
      <p class="dish__desc">Hühnerfleisch | Spinat | Saisongemüse | Sesam</p>
    </article>
  </section>

  <!-- Vorspeisen: Salate -->
  <section class="page page--tr">
    <div class="rule" style="left:47px; width:83px;"></div>
    <div class="brand"><span class="brand__name">HOSHIBA</span><span class="brand__square"></span></div>
    <div class="rule" style="left:200px; width:79px;"></div>

    <div class="section-label" style="top:200px;">SALAD</div>

    <article class="dish" style="top:255px;">
      <div class="dish__head"><span class="dish__name">MIEN – GLASNUDELSALAT</span><span class="dish__price">6,5</span></div>
      <p class="dish__desc">Frühlingszwiebel | Karotte | Koriander | Minze | Erdnüsse |<br>Lauch | Limetten-Dressing<br>wahlweise mit Tofu | <span class="caps">H</span>ühnerfleisch | Rindfleisch</p>
    </article>
    <article class="dish" style="top:334px;">
      <div class="dish__head"><span><span class="dish__name">LAAB GAI</span> <span class="dish__note">– LEICHT SCHARF</span></span><span class="dish__price">8,5</span></div>
      <p class="dish__desc">Hühnerfleischfilet | Rote Zwiebel | Minze | Duftreis |<br>Paprika | Frühlingszwiebel | Koriander</p>
    </article>
    <article class="dish" style="top:413px;">
      <div class="dish__head"><span><span class="dish__name">NAM TOK NUKA</span> <span class="dish__note">– SCHARF</span></span><span class="dish__price">9,5</span></div>
      <p class="dish__desc">Rindfleischfilet | Rote Zwiebel | Minze | Duftreis |<br>Paprika | Frühlingszwiebel | Koriander</p>
    </article>
  </section>

  <!-- Sushi: Maki -->
  <section class="page page--bl">
    <div class="rule" style="left:46px; width:88px;"></div>
    <div class="script-title" role="img" aria-label="Handgeschriebener Schriftzug „sushi“" style="left:136px; width:50px;"></div>
    <div class="rule" style="left:189px; width:89px;"></div>
    <p class="section-intro">Nori · Reis · Fisch / Gemüse</p>

    <div class="section-label" style="top:199px;">MAKI</div>

    <article class="dish" style="top:263px;">
      <div class="dish__head"><span class="dish__name">SAKE AVO</span><span class="dish__price">7,5</span></div>
      <p class="dish__desc">Lachs Avocado | 6 Stück</p>
    </article>
    <article class="dish" style="top:315px;">
      <div class="dish__head"><span class="dish__name">TEKKA</span><span class="dish__price">6,5</span></div>
      <p class="dish__desc">Thunfisch | 6 Stück</p>
    </article>
    <article class="dish" style="top:368px;">
      <div class="dish__head"><span class="dish__name">UNAGI</span><span class="dish__price">6,0</span></div>
      <p class="dish__desc">Aal | 6 Stück</p>
    </article>

    <div class="illustration" role="img" aria-label="Linienzeichnung: Essstäbchen mit einem Maki-Röllchen"></div>
  </section>

  <!-- Sushi: Inside Out -->
  <section class="page page--br">
    <div class="rule" style="left:47px; width:83px;"></div>
    <div class="brand"><span class="brand__name">HOSHIBA</span><span class="brand__square"></span></div>
    <div class="rule" style="left:200px; width:79px;"></div>

    <article class="dish" style="top:263px;">
      <div class="dish__head"><span class="dish__name">CALIFORNIA INSIDE OUT</span><span class="dish__price">8,5</span></div>
      <p class="dish__desc">innen Garnele aussen Fischrogen | 4 Stück</p>
    </article>
    <article class="dish" style="top:315px;">
      <div class="dish__head"><span class="dish__name">CALIFORNIA INSIDE OUT</span><span class="dish__price">7,0</span></div>
      <p class="dish__desc">innen Surimi aussen Fischrogen | 4 Stück</p>
    </article>
    <article class="dish" style="top:368px;">
      <div class="dish__head"><span class="dish__name">CALIFORNIA INSIDE OUT</span><span class="dish__price">7,5</span></div>
      <p class="dish__desc">innen Lachs aussen Fischrogen | 4 Stück</p>
    </article>
  </section>

</div>
</body>
</html>
```